Brightwave Travel and Tours

Hotel Reservations
Airline Ticketing
Day Tour

My business is a Travel agency. My services are issuing domestic and international tickets. Book room/hotel reservations local/international.
My color preference is apple green/orange/red/blue.
Images of beaches, tickets,luggage.

```html
<!DOCTYPE html>
<html lang="en">
<head>
<meta charset="utf-8">
<title>Brightwave Travel and Tours – Business Card</title>
<link href="https://fonts.googleapis.com/css2?family=Open+Sans:wght@400;600;700&display=swap" rel="stylesheet">
<style>
  :root {
    --stage: #1d1d1f;
    --brand-blue: #1f7fd1;
    --brand-blue-light: #3ea6e3;
    --brand-blue-deep: #1668b8;
    --ink-teal: #1b6f8e;
    --accent-yellow: #f2e52e;
    --card-white: #ffffff;
    --text-dark: #3a3a3a;
    --divider: #c9d3dc;
  }
  * { margin: 0; padding: 0; box-sizing: border-box; }
  html, body {
    width: 1200px; height: 900px; overflow: hidden;
    background: var(--stage);
    font-family: "Open Sans", Arial, sans-serif;
  }
  .stage { position: relative; width: 1200px; height: 900px; }
  .card {
    position: absolute; left: 320px; width: 560px; height: 320px;
    overflow: hidden; border-radius: 2px;
    box-shadow: 0 18px 40px rgba(0,0,0,.55);
  }
  .card-front {
    top: 90px;
    background: linear-gradient(100deg, var(--brand-blue-deep) 0%, var(--brand-blue) 45%, var(--brand-blue-light) 100%);
  }
  .card-back { top: 490px; background: var(--card-white); }

  .brand { position: absolute; display: flex; flex-direction: column; align-items: center; }
  .brand-mark { width: 64px; height: 64px; border-radius: 50%; margin-bottom: 12px; }
  .brand-name {
    font-weight: 700; font-size: 24px; letter-spacing: 1px;
    text-transform: uppercase; text-align: center; line-height: 1.1;
  }
  .card-front .brand { left: 0; right: 0; top: 86px; }
  .card-front .brand-mark { border: 4px solid var(--card-white); }
  .card-front .brand-name { color: var(--card-white); }

  .card-back .brand { left: 30px; width: 250px; top: 90px; }
  .card-back .brand-mark { background: var(--brand-blue-light); }
  .card-back .brand-name { color: var(--ink-teal); font-size: 21px; }

  .card-decor { position: absolute; left: 0; bottom: 0; }

  .contact {
    position: absolute; left: 298px; top: 42px; width: 240px;
    padding-left: 20px; border-left: 1px solid var(--divider);
    height: 150px;
  }
  .contact-name { color: var(--brand-blue); font-weight: 600; font-size: 20px; line-height: 1.2; }
  .contact-role { color: var(--text-dark); font-size: 15px; margin-bottom: 18px; }
  .contact-list { list-style: none; }
  .contact-item {
    display: flex; align-items: center; gap: 9px;
    color: var(--text-dark); font-size: 14px; line-height: 24px;
    white-space: nowrap;
  }
  .contact-item svg { width: 13px; height: 13px; flex: none; }
</style>
</head>
<body>
<main class="stage">

  <section class="card card-front" aria-label="Card front">
    <div class="brand">
      <span class="brand-mark" aria-hidden="true"></span>
      <p class="brand-name">Brightwave<br>Travel and Tours</p>
    </div>
  </section>

  <section class="card card-back" aria-label="Card back">
    <svg class="card-decor" width="560" height="320" viewBox="0 0 560 320" aria-hidden="true">
      <path d="M0 300 L560 262 L560 320 L0 320 Z" fill="var(--brand-blue)"/>
      <path d="M0 310 L560 290 L560 320 L0 320 Z" fill="var(--brand-blue)"/>
      <path d="M385 320 C395 272 430 252 480 250 L560 246 L560 320 Z" fill="var(--accent-yellow)"/>
    </svg>

    <div class="brand">
      <span class="brand-mark" aria-hidden="true"></span>
      <p class="brand-name">Brightwave<br>Travel and Tours</p>
    </div>

    <div class="contact">
      <h1 class="contact-name">Dana Whitfield</h1>
      <p class="contact-role">Manager</p>
      <ul class="contact-list">
        <li class="contact-item">
          <svg viewBox="0 0 16 16" aria-hidden="true"><path d="M3 1l3 3-1.5 2a9 9 0 005 5l2-1.5 3 3-2 2C6 14 2 10 1 3z" fill="var(--brand-blue)"/></svg>
          555 014 2270
        </li>
        <li class="contact-item">
          <svg viewBox="0 0 16 16" aria-hidden="true"><g fill="none" stroke="var(--brand-blue)" stroke-width="1.4"><circle cx="8" cy="8" r="6.5"/><ellipse cx="8" cy="8" rx="3" ry="6.5"/><path d="M1.5 8h13"/></g></svg>
          www.danawhitfield.com
        </li>
        <li class="contact-item">
          <svg viewBox="0 0 16 16" aria-hidden="true"><text x="8" y="13" text-anchor="middle" font-size="14" font-weight="700" fill="var(--brand-blue)" font-family="Open Sans, sans-serif">@</text></svg>
          dana@brightwavetravel.com
        </li>
      </ul>
    </div>
  </section>

</main>
</body>
</html>
```